Business card design needed

am looking for a fun and funky design to match our moto, seriously fun swimwear and fashion for girls.

We manufacture and retail girls swimwear and fashion in Australia. Our designs are fun loving and funky. I would like to use bright fuschia to match our website www.breezyplum.com.au. We target a higher end market so need it to reflect this.

Industry/Entity Type

Fashion

Contact Information for Business Card

Breezy Plum logo,
Maddie Lorne
(07) 35517204
admin@breezyplum.com.au
www.breezyplum.com.au

Logo Text

Breezy Plum

```html
<!DOCTYPE html>
<html lang="en">
<head>
<meta charset="utf-8">
<title>Breezy Plum – Business Card</title>
<link rel="stylesheet" href="https://fonts.googleapis.com/css2?family=Cormorant+Garamond:wght@500&display=swap">
<style>
  :root {
    --fuchsia-deep: #a8125f;
    --fuchsia: #d42683;
    --fuchsia-soft: #e86aa9;
    --blush: #f5b8d6;
    --petal: #fbe2ef;
    --paper: #ffffff;
    --text: #c02474;
  }
  * { margin: 0; padding: 0; box-sizing: border-box; }
  html, body { width: 1200px; height: 694px; overflow: hidden; background: var(--paper); }
  .card {
    position: relative;
    width: 1200px;
    height: 694px;
    background: var(--paper);
    font-family: "Cormorant Garamond", "Times New Roman", serif;
    color: var(--text);
  }
  .pattern-band {
    position: absolute;
    left: 0;
    width: 1200px;
    height: 78px;
    background: linear-gradient(90deg, var(--fuchsia-soft), var(--fuchsia) 25%, var(--blush) 50%, var(--fuchsia) 75%, var(--fuchsia-soft));
  }
  .pattern-band--top { top: 0; }
  .pattern-band--bottom { bottom: 0; }
  .sheen { position: absolute; left: 0; width: 1200px; height: 62px; }
  .sheen--top {
    top: 78px;
    background:
      radial-gradient(ellipse 55% 90% at 50% 55%, rgba(255,255,255,0.8), rgba(255,255,255,0) 70%),
      linear-gradient(to bottom, var(--fuchsia-deep), var(--fuchsia) 35%, var(--blush) 72%, var(--paper));
  }
  .sheen--bottom {
    bottom: 78px;
    background:
      radial-gradient(ellipse 55% 90% at 50% 45%, rgba(255,255,255,0.8), rgba(255,255,255,0) 70%),
      linear-gradient(to top, var(--fuchsia-deep), var(--fuchsia) 35%, var(--blush) 72%, var(--paper));
  }
  .contact {
    position: absolute;
    top: 150px;
    left: 0;
    width: 1200px;
    text-align: center;
  }
  .contact__name {
    font-size: 48px;
    font-weight: 500;
    letter-spacing: 4px;
    text-transform: uppercase;
    line-height: 58px;
  }
  .contact__line {
    font-size: 52px;
    letter-spacing: 1px;
    line-height: 64px;
  }
  .contact__dot { padding: 0 12px; }
  .brand__mark {
    position: absolute;
    left: 290px;
    top: 356px;
    width: 104px;
    height: 104px;
    border-radius: 50%;
    background: var(--fuchsia);
  }
  .brand__name {
    position: absolute;
    left: 424px;
    top: 400px;
    font-size: 96px;
    font-weight: 500;
    line-height: 1;
    color: var(--text);
    white-space: nowrap;
  }
</style>
</head>
<body>
<main class="card">
  <div class="pattern-band pattern-band--top" role="img" aria-label="Decorative band of pink and fuchsia candy stripes"></div>
  <div class="sheen sheen--top"></div>

  <section class="contact">
    <h1 class="contact__name">Maddie Lorne</h1>
    <p class="contact__line">(07) 35517204<span class="contact__dot">•</span>admin@breezyplum.com.au</p>
    <p class="contact__line">www.breezyplum.com.au</p>
  </section>

  <span class="brand__mark"></span>
  <span class="brand__name">Breezy Plum</span>

  <div class="sheen sheen--bottom"></div>
  <div class="pattern-band pattern-band--bottom" role="img" aria-label="Decorative band of pink and fuchsia candy stripes"></div>
</main>
</body>
</html>
```